Looking for a Micropage Template

My website will be offering our users to have their very own micropage / profile page hosted on our website.

I am looking for someone to design a a web micropage / profile template that matches the color theme of our websites homepage.

1. Follow the colors of our homepage

2. Open the excel sheet and follow the directions to design a micropage / profile page template.

Target Market(s)

Travel Market

Industry/Entity Type

Travel

Number of Pages Required

1 page

Requirements
Must have
• All of the fields specified in the excel sheet
Nice to have
• Follow the color themes and style of the company homepage
• Different color themes is acceptable as long as it looks nice
• Nice HQ photos

```html
<!DOCTYPE html>
<html lang="en">
<head>
<meta charset="utf-8">
<title>Voyara – Micropage</title>
<link href="https://fonts.googleapis.com/css2?family=Open+Sans:ital,wght@0,400;0,600;0,700;1,400&family=Quicksand:wght@300;400;500&display=swap" rel="stylesheet">
<style>
  :root{
    --nav-dark:#2a2a2a;
    --nav-active:#3a3a3a;
    --accent:#f2cb1d;
    --band:#e7c52a;
    --paper:#efefef;
    --paper-alt:#f6f6f6;
    --ink:#2e2e2e;
    --muted:#777;
    --footer:#323232;
    --footer-deep:#262626;
    --footer-text:#bdbdbd;
    --white:#fff;
  }
  *{box-sizing:border-box;margin:0;padding:0}
  html,body{width:750px;height:1200px;overflow:hidden}
  body{position:relative;font-family:"Open Sans",Arial,sans-serif;color:var(--ink);background:var(--paper)}
  .abs{position:absolute}

  /* header */
  .site-header{position:absolute;left:0;top:0;width:750px;height:50px;background:var(--nav-dark)}
  .brand{position:absolute;left:108px;top:14px;display:flex;align-items:center;gap:6px;color:var(--accent);font-weight:700;font-size:17px;letter-spacing:.3px}
  .brand-dot{width:10px;height:10px;border-radius:50%;background:var(--accent)}
  .main-nav{position:absolute;left:341px;top:0;height:50px;display:flex;list-style:none}
  .main-nav li{height:50px;display:flex;align-items:center;padding:0 11px;color:var(--white);font-size:7.5px;font-weight:700;letter-spacing:.2px}
  .main-nav li.is-active{background:var(--nav-active);border-top:3px solid var(--accent);padding-bottom:3px}

  /* hero */
  .hero{position:absolute;left:0;top:50px;width:750px;height:228px;
    background:linear-gradient(180deg,#5f93c8 0%,#9cc2e2 38%,#d7e6ef 55%,#38b4c0 64%,#7fcfcc 70%,#e9e2d2 78%,#f1ece3 100%)}
  .hero-rule{position:absolute;left:266px;width:204px;border-top:1px dotted rgba(255,255,255,.8)}
  .hero-title{position:absolute;left:0;width:750px;top:126px;text-align:center;color:var(--white);font-size:28px;font-weight:400}

  /* booking bar */
  .booking{position:absolute;left:120px;top:254px;width:510px;height:50px;background:var(--nav-dark);box-shadow:0 8px 12px -6px rgba(0,0,0,.45)}
  .field{position:absolute;top:6px;width:126px}
  .field label{display:block;color:var(--accent);font-size:9px;line-height:11px}
  .field .input{margin-top:2px;height:21px;background:var(--white);border-radius:3px;color:#999;font-size:9.5px;padding:4px 5px;display:flex;align-items:center;gap:3px}
  .btn{display:flex;align-items:center;justify-content:center;background:var(--accent);color:var(--ink);font-weight:700;border-radius:3px}
  .booking .btn{position:absolute;left:413px;top:17px;width:88px;height:23px;font-size:9px}

  /* intro */
  .intro{position:absolute;left:0;top:304px;width:750px;height:224px;background:var(--paper);border-bottom:1px solid #d4d4d4}
  .section-title{position:absolute;left:0;width:750px;text-align:center;font-size:19px;font-weight:400;color:var(--ink)}
  .intro p{position:absolute;left:88px;top:51px;width:574px;text-align:center;font-size:7.3px;line-height:10px;color:var(--muted)}
  .carousel-arrow{position:absolute;top:134px}
  .circle{position:absolute;top:98px;width:108px;height:108px;border-radius:50%;border:2px solid #222}

  /* offers */
  .offers{position:absolute;left:0;top:529px;width:750px;height:399px;background:var(--paper-alt)}
  .card{position:absolute;width:190px}
  .card .photo{height:78px;border:1px solid #333}
  .card h3{margin-top:2px;text-align:center;font-size:12px;font-weight:400;color:#444;letter-spacing:.4px}
  .card p{text-align:center;font-size:6.3px;line-height:8.5px;color:var(--muted);margin-top:1px}
  .amenities{display:flex;justify-content:center;gap:4px;margin-top:6px}
  .amenities svg{width:10px;height:10px}

  /* quote band */
  .quote-band{position:absolute;left:0;top:928px;width:750px;height:92px;background:var(--band)}
  .quote-band h2{position:absolute;left:91px;top:21px;font-family:"Quicksand",sans-serif;font-weight:400;font-size:23px;color:var(--white);letter-spacing:1px}
  .quote-band blockquote{position:absolute;left:91px;top:61px;font-size:8px;font-style:italic;color:var(--white)}
  .figure{position:absolute;left:546px;top:890px;width:126px;height:130px;background:linear-gradient(180deg,#1a1a1a,#050505);border-radius:40px 40px 0 0}

  /* footer */
  .site-footer{position:absolute;left:0;top:1020px;width:750px;height:180px;background:var(--footer)}
  .footer-base{position:absolute;left:0;bottom:0;width:750px;height:12px;background:var(--footer-deep)}
  .col{position:absolute;top:42px;color:var(--footer-text);font-size:6.4px;line-height:8.5px}
  .col h4{color:var(--white);font-size:8.5px;font-weight:400;margin-bottom:9px;letter-spacing:.3px}
  .col p{margin-bottom:7px}
  .news li{list-style:none;margin-bottom:6px;color:var(--footer-text)}
  .news small{display:block;color:#8a8a8a;font-size:5.5px}
  .login label{display:block;margin-top:2px}
  .login .input{height:12px;width:100px;background:#2a2a2a;border:1px solid #444;border-radius:2px;margin:3px 0 6px}
  .col .btn{height:13px;font-size:6px;border-radius:4px}
</style>
</head>
<body>
<svg width="0" height="0" style="position:absolute">
  <symbol id="i-fan" viewBox="0 0 10 10"><circle cx="5" cy="5" r="1.3" fill="#333"/><path d="M5 4C4 1 6 0 7 1S6 4 5 4ZM6 5C9 4 10 6 9 7S6 6 6 5ZM4 6C1 6 1 8 2 9S4 7 4 6Z" fill="#333"/></symbol>
  <symbol id="i-flag" viewBox="0 0 10 10"><path d="M2 1V9.5" stroke="#333" stroke-width="1.2"/><path d="M2.5 1.5H8L6.8 3.5 8 5.5H2.5Z" fill="#333"/></symbol>
  <symbol id="i-plane" viewBox="0 0 10 10"><path d="M1 6L9 3.2 9.5 4 5.5 6 6 9 5 9 3.8 6.6 1.6 7.4Z" fill="#333"/></symbol>
  <symbol id="i-tv" viewBox="0 0 10 10"><rect x="1" y="2" width="8" height="5.5" fill="none" stroke="#333" stroke-width="1.1"/><path d="M3 9H7" stroke="#333" stroke-width="1"/></symbol>
  <symbol id="i-wifi" viewBox="0 0 10 10"><path d="M1 4.5A6 6 0 0 1 9 4.5M2.5 6A4 4 0 0 1 7.5 6M4 7.5A2 2 0 0 1 6 7.5" fill="none" stroke="#333" stroke-width="1"/><circle cx="5" cy="8.6" r=".7" fill="#333"/></symbol>
  <symbol id="i-cup" viewBox="0 0 10 10"><path d="M1.5 4H7.5V7A2 2 0 0 1 5.5 9H3.5A2 2 0 0 1 1.5 7Z" fill="#333"/><path d="M7.5 5H8.5V7H7.5" fill="none" stroke="#333" stroke-width=".8"/><path d="M3 1.5V3M5 1V3" stroke="#333" stroke-width=".7"/></symbol>
  <symbol id="i-cal" viewBox="0 0 10 10"><rect x="1" y="2" width="8" height="7" fill="#777"/><rect x="2" y="4" width="6" height="4" fill="#fff"/></symbol>
</svg>

<header class="site-header">
  <div class="brand"><span class="brand-dot"></span>Voyara</div>
  <ul class="main-nav">
    <li class="is-active">START</li>
    <li>FACILITIES</li>
    <li>RESTAURANT</li>
    <li>CONFERENCE</li>
    <li>BOOKINGS</li>
    <li>CONTACT US</li>
  </ul>
</header>

<section class="hero" role="img" aria-label="Family walking hand in hand along a sunny tropical beach">
  <div class="hero-rule" style="top:68px"></div>
  <h1 class="hero-title" style="top:78px">Lorem Ipsum</h1>
  <div class="hero-rule" style="top:125px"></div>
</section>

<form class="booking">
  <div class="field" style="left:10px"><label>Arrival</label><div class="input"><svg width="7" height="7"><use href="#i-cal"/></svg>21/08/2013</div></div>
  <div class="field" style="left:145px"><label>Departure</label><div class="input"><svg width="7" height="7"><use href="#i-cal"/></svg>22/08/2013</div></div>
  <div class="field" style="left:280px"><label>Lorem Ipsum</label><div class="input"><svg width="7" height="7" viewBox="0 0 10 10"><path d="M2 3L5 7 8 3" fill="none" stroke="#555" stroke-width="1.6"/></svg>Standard Single Room</div></div>
  <div class="btn">View Prices</div>
</form>

<section class="intro">
  <h2 class="section-title" style="top:22px">Lorem Ipsum</h2>
  <p>Sed euismod sem id consequat rutrum. Ut convallis lorem a orci mollis, eu vulputate libero aliquet. Praesent egestas nisi sed purus tincidunt faucibus. Aliquam lobortis orci lacus, sed faucibus augue dapibus vitae. Ut vitae mi sapien. Phasellus a eros justo. Curabitur odio massa, tincidunt nec nibh sit amet.</p>
  <svg class="carousel-arrow" style="left:120px" width="26" height="40" viewBox="0 0 26 40"><path d="M22 4L6 20 22 36" fill="none" stroke="#2b2b2b" stroke-width="7" stroke-linejoin="round"/></svg>
  <div class="circle" role="img" aria-label="Hotel bedroom with warm lamps" style="left:199px;background:radial-gradient(circle at 40% 60%,#f0e2b8,#8a6a3a 70%,#4a3520)"></div>
  <div class="circle" role="img" aria-label="Resort terrace at dusk" style="left:319px;background:radial-gradient(circle at 50% 70%,#f3a848,#8a5a7a 60%,#3c2d4e)"></div>
  <div class="circle" role="img" aria-label="Waiter serving guests at a restaurant table" style="left:439px;background:radial-gradient(circle at 50% 50%,#f4efe6,#b9876a 60%,#5a4032)"></div>
  <svg class="carousel-arrow" style="left:600px" width="26" height="40" viewBox="0 0 26 40"><path d="M4 4L20 20 4 36" fill="none" stroke="#2b2b2b" stroke-width="7" stroke-linejoin="round"/></svg>
</section>

<section class="offers">
  <h2 class="section-title" style="top:17px">Lorem Ipsum</h2>

  <article class="card" style="left:80px;top:67px">
    <div class="photo" role="img" aria-label="Airliner silhouette against a sunset sky" style="background:linear-gradient(180deg,#d23a12,#f5861c 55%,#f9c04a)"></div>
    <h3>Lorem Ipsum</h3>
    <p>Lorem ipsum dolor sit amet, consectetur adipiscing elit. Praesent scelerisque lectus vitae dui sollicitudin commodo.</p>
    <div class="amenities"><svg><use href="#i-fan"/></svg><svg><use href="#i-flag"/></svg><svg><use href="#i-plane"/></svg><svg><use href="#i-tv"/></svg><svg><use href="#i-wifi"/></svg><svg><use href="#i-cup"/></svg></div>
  </article>
  <article class="card" style="left:280px;top:67px">
    <div class="photo" role="img" aria-label="Hikers on a hilltop overlooking a green valley" style="background:linear-gradient(180deg,#8fc3e4,#bcd9ea 45%,#5f8f6a 75%,#4a6b44)"></div>
    <h3>Lorem Ipsum</h3>
    <p>Lorem ipsum dolor sit amet, consectetur adipiscing elit. Praesent scelerisque lectus vitae dui sollicitudin commodo.</p>
    <div class="amenities"><svg><use href="#i-fan"/></svg><svg><use href="#i-flag"/></svg><svg><use href="#i-plane"/></svg><svg><use href="#i-tv"/></svg><svg><use href="#i-wifi"/></svg><svg><use href="#i-cup"/></svg></div>
  </article>
  <article class="card" style="left:480px;top:67px">
    <div class="photo" role="img" aria-label="City skyline floating on a globe over the sea" style="background:linear-gradient(180deg,#d9ecf7,#7fb6dd 50%,#2f7fc0)"></div>
    <h3>Lorem Ipsum</h3>
    <p>Lorem ipsum dolor sit amet, consectetur adipiscing elit. Praesent scelerisque lectus vitae dui sollicitudin commodo.</p>
    <div class="amenities"><svg><use href="#i-fan"/></svg><svg><use href="#i-flag"/></svg><svg><use href="#i-plane"/></svg><svg><use href="#i-tv"/></svg><svg><use href="#i-wifi"/></svg><svg><use href="#i-cup"/></svg></div>
  </article>

  <article class="card" style="left:80px;top:217px">
    <div class="photo" role="img" aria-label="World landmarks gathered on a globe under a blue sky" style="background:linear-gradient(180deg,#58a8e0,#a7d3ef 50%,#6fae5a 80%,#3d7fbe)"></div>
    <h3>Lorem Ipsum</h3>
    <p>Lorem ipsum dolor sit amet, consectetur adipiscing elit. Praesent scelerisque lectus vitae dui sollicitudin commodo.</p>
    <div class="amenities"><svg><use href="#i-fan"/></svg><svg><use href="#i-flag"/></svg><svg><use href="#i-plane"/></svg><svg><use href="#i-tv"/></svg><svg><use href="#i-wifi"/></svg><svg><use href="#i-cup"/></svg></div>
  </article>
  <article class="card" style="left:280px;top:217px">
    <div class="photo" role="img" aria-label="Backpacker resting beside a country road" style="background:linear-gradient(180deg,#d8cf9a,#9a8a55 50%,#5d5a36)"></div>
    <h3>Lorem Ipsum</h3>
    <p>Lorem ipsum dolor sit amet, consectetur adipiscing elit. Praesent scelerisque lectus vitae dui sollicitudin commodo.</p>
    <div class="amenities"><svg><use href="#i-fan"/></svg><svg><use href="#i-flag"/></svg><svg><use href="#i-plane"/></svg><svg><use href="#i-tv"/></svg><svg><use href="#i-wifi"/></svg><svg><use href="#i-cup"/></svg></div>
  </article>
  <article class="card" style="left:480px;top:217px">
    <div class="photo" role="img" aria-label="Mountaineer gear against a clear blue sky" style="background:linear-gradient(90deg,#7a2e2e,#3d4f8e 40%,#3f6fd0 70%,#8fb4ec)"></div>
    <h3>Lorem Ipsum</h3>
    <p>Lorem ipsum dolor sit amet, consectetur adipiscing elit. Praesent scelerisque lectus vitae dui sollicitudin commodo.</p>
    <div class="amenities"><svg><use href="#i-fan"/></svg><svg><use href="#i-flag"/></svg><svg><use href="#i-plane"/></svg><svg><use href="#i-tv"/></svg><svg><use href="#i-wifi"/></svg><svg><use href="#i-cup"/></svg></div>
  </article>
</section>

<section class="quote-band">
  <h2>Lorem Ipsum dolor amit</h2>
  <blockquote>“Hospitality, Quality &amp; Good Locations. We only provide you with the best hotels” - Sam Carter</blockquote>
</section>
<div class="figure" role="img" aria-label="Dark silhouette of a host in a suit"></div>

<footer class="site-footer">
  <div class="col" style="left:91px;width:100px">
    <h4>ABOUT US</h4>
    <p>Suspendisse erat mi, tincidunt sit amet massa quis, commodo fermentum diam. Sed nec dui nec nunc tempor interdum.</p>
    <p>Ut vulputate augue urna, ut porta dolor imperdiet a. Vestibulum nec leo eu magna aliquam ornare.</p>
  </div>
  <div class="col news" style="left:211px;width:80px">
    <h4>LATEST NEWS</h4>
    <ul>
      <li>Lorem Ipsum<small>15 AUG</small></li>
      <li>Lorem Ipsum<small>15 AUG</small></li>
      <li>Lorem Ipsum<small>15 AUG</small></li>
      <li>Lorem Ipsum<small>15 AUG</small></li>
    </ul>
  </div>
  <div class="col" style="left:332px;width:230px">
    <h4>JOIN US</h4>
    <p>Cum sociis natoque penatibus et magnis dis parturient montes, nascetur ridiculus mus. Phasellus sed lorem blandit egestas. Nam id lectus vel orci luctus consectetur eget id elit. In tortor odio, pellentesque eu orci sit amet, lacinia euismod nisl. Aliquam sodales tristique mauris ac fermentum. Donec vel varius quam. Pellentesque vitae mollis massa.</p>
    <p>There is no costs or whatsoever so sign up today!</p>
    <div class="btn" style="width:52px;margin-top:8px">READ MORE</div>
  </div>
  <div class="col login" style="left:571px;width:110px">
    <h4>CONTACT US</h4>
    <label>Username</label><div class="input"></div>
    <label>Password</label><div class="input"></div>
    <div class="btn" style="width:52px;margin-top:6px">LOGIN</div>
  </div>
  <div class="footer-base"></div>
</footer>
</body>
</html>
```